VELQUARTH - A modern gin bottle label

Design of a bottle label in a modern fresh design. The name of the gin is "VELQUARTH Hollow Batch K7". Please take a look at the velquarth.de website. on the main page of velquarth.de you can breathe the design direction here: 1) the taste of the gin should be composed of 10 botanicals ... an important scent note. ) a distinctive flavor is spicy and fresh 3.) The filling volume is 0.5 liters 4.) the alcohol content is 43% vol. 5.) the variety is called "dry gin" 6.) velquarth stands for "energy" and "love"

Target Market(s)

Alcohol consumer

Colors

Designer to choose colors to be used in the design.

Requirements
Must have
• the velquarth corporate logo must be included, the name of the gin is "VELQUARTH Hollow Batch K7"
Nice to have
• Please use the bottles template in the appendix. (The Black Bottles) they can use the saying "DESTILLED & BOTTLED BY OLD MARROW" in small letters

```html
<!DOCTYPE html>
<html lang="en">
<head>
<meta charset="utf-8">
<title>VELQUARTH Hollow Batch K7 – Label</title>
<link href="https://fonts.googleapis.com/css2?family=Montserrat:wght@700&family=Oswald:wght@300;400;700&family=Playfair+Display:wght@700&display=swap" rel="stylesheet">
<style>
  :root {
    --backdrop: #1c1c1e;
    --label-edge: #1b1b1b;
    --label-panel: #0e0e0e;
    --rule: #3a3a3a;
    --ink: #ffffff;
    --muted: #5a5a5a;
    --accent: #f26a0c;
    --badge-ink: #1a0d04;
  }
  * { box-sizing: border-box; margin: 0; padding: 0; }
  html, body {
    width: 776px; height: 1200px; overflow: hidden;
    background: var(--backdrop);
  }
  .label {
    position: absolute; left: 38px; top: 178px;
    width: 700px; height: 844px;
    background: var(--label-edge);
  }
  .label__panel {
    position: absolute; inset: 29px;
    background: var(--label-panel);
  }
  .label__frame { position: absolute; left: 0; top: 0; }
  .wordmark {
    position: absolute; left: 0; right: 0; top: 212px;
    text-align: center;
    font-family: "Montserrat", sans-serif; font-weight: 700;
    font-size: 50px; letter-spacing: 7px; line-height: 1;
    color: var(--ink);
  }
  .edition {
    position: absolute; left: 0; right: 0; top: 320px;
    text-align: center;
    font-family: "Oswald", sans-serif; font-weight: 700;
    font-size: 168px; line-height: 143px; letter-spacing: -2px;
    color: var(--ink); text-transform: uppercase;
  }
  .badge {
    position: absolute; left: 521px; top: 581px;
    width: 92px; height: 92px; border-radius: 50%;
    background: var(--accent);
    display: flex; align-items: center; justify-content: center;
    font-family: "Playfair Display", serif; font-weight: 700;
    font-size: 46px; color: var(--badge-ink);
  }
  .spec {
    position: absolute; top: 646px; width: 200px;
    text-align: center; color: var(--ink);
    font-family: "Oswald", sans-serif;
  }
  .spec--volume { left: 156px; }
  .spec--alcohol { left: 342px; }
  .spec__name { font-weight: 400; font-size: 19px; line-height: 24px; letter-spacing: -0.3px; }
  .spec__value { font-weight: 300; font-size: 35px; line-height: 42px; }
  .maker {
    position: absolute; left: 0; right: 0; top: 744px;
    text-align: center;
    font-family: "Oswald", sans-serif; font-weight: 400;
    font-size: 12px; letter-spacing: 6px;
    color: var(--muted);
  }
</style>
</head>
<body>
  <section class="label" aria-label="VELQUARTH Hollow Batch K7 bottle label">
    <div class="label__panel"></div>
    <svg class="label__frame" width="700" height="844" viewBox="0 0 700 844" aria-hidden="true">
      <g stroke="var(--rule)" stroke-width="1.2" fill="none">
        <line x1="116" y1="50" x2="584" y2="50"/>
        <line x1="116" y1="64" x2="584" y2="64"/>
        <line x1="116" y1="781" x2="584" y2="781"/>
        <line x1="116" y1="794" x2="584" y2="794"/>
        <line x1="64" y1="114" x2="64" y2="713"/>
        <line x1="77" y1="114" x2="77" y2="713"/>
        <line x1="636" y1="114" x2="636" y2="713"/>
        <line x1="623" y1="114" x2="623" y2="713"/>
      </g>
    </svg>

    <h1 class="wordmark">VELQUARTH</h1>
    <p class="edition">Hollow<br>Batch</p>
    <div class="badge">K7</div>

    <div class="spec spec--volume">
      <p class="spec__name">Filling Volume</p>
      <p class="spec__value">0.5 liters</p>
    </div>
    <div class="spec spec--alcohol">
      <p class="spec__name">Alcohol Content</p>
      <p class="spec__value">43% vol.</p>
    </div>

    <p class="maker">Destilled &amp; Bottled By Old Marrow</p>
  </section>
</body>
</html>
```